Merlow Coaching flyer (women local)

Strapline: Do you want a more fulfilling and meaningful life?
Make 2015 a year for positive change

Image of an attractive woman in contemplation:

• I’ve lost my identity and wondering what life is about.

• I want more intimacy in my relationship

• I hate my career and don’t know what’s right for me

Personal Development Coaching can help you:

Testimonials from our clients:

‘I have changed the way I approach my daily life in order to achieve more for myself’.

‘Coaching has helped me change the way I think, focusing more on positive rather than negative thoughts’.

‘Without coaching, I believe that my life would have remained stagnant’.

‘ I have made the leap to set up my own business and have increased my income three fold’.

‘Coaching has helped me to grow closer than ever to my husband’.

Any relevant image and image of myself (included)

Why Merlow?

• Certified Personal Development Coach

• Experience coaching individuals wanting to effect change

Joan is a specialist in coaching for:

• Building confidence

• Feeling motivated and getting out of a rut

• Enhancing relationships with partners or family

• Making changes in your career or business

Book your free consultation (this should stand out)

e: joan@merlow-example.co.uk t: 0784 512 6037 w: www.merlow-example.co.uk (include logo, but change ‘Merlow Consulting’ to ‘Merlow Coaching’)
f: www.facebook.com/merlow-example.co.uk t: @jkmerlow

* Notes in brackets are only instructions and not to be included as part of the flyer.
Updates

Flyer is is A5

Please not this flyer can be double sided as I feel there will be too much text for one side. Could you use image of woman in contemplation on front but not too depressing.

```html
<!DOCTYPE html>
<html lang="en">
<head>
<meta charset="utf-8">
<title>Merlow Coaching – Flyer</title>
<link rel="stylesheet" href="https://fonts.googleapis.com/css2?family=Andada+Pro:ital,wght@0,400;1,400&family=Kreon:wght@300;400&display=swap">
<style>
  :root {
    --cyan: #1cb2dc;
    --navy: #1f2d62;
    --purple: #7c3f97;
    --quote: #7a3d90;
    --paper: #ffffff;
    --paper-end: #efeff2;
    --stage: #eceff1;
    --photo-light: #ece4dc;
    --photo-mid: #d8c2aa;
    --photo-dark: #b99577;
  }
  * { margin: 0; padding: 0; box-sizing: border-box; }
  html, body { width: 1040px; height: 1200px; overflow: hidden; }
  body { background: var(--stage); position: relative; font-family: "Andada Pro", Georgia, serif; }

  .flyer {
    position: absolute; left: 130px; top: 48px;
    width: 780px; height: 1103px; overflow: hidden;
    background: linear-gradient(180deg, var(--paper) 55%, var(--paper-end) 100%);
  }
  .hero-photo {
    position: absolute; left: 0; top: 0; width: 780px; height: 523px;
    background:
      radial-gradient(ellipse 260px 300px at 200px 300px, var(--photo-mid), transparent 75%),
      linear-gradient(100deg, var(--photo-dark) 0%, var(--photo-mid) 35%, var(--photo-light) 70%, #f4f1ee 100%);
  }
  .hero-band { position: absolute; left: 0; top: 521px; width: 780px; height: 5px; background: var(--cyan); }

  .brand { position: absolute; left: 548px; top: 40px; width: 200px; text-align: center; color: var(--navy); font-family: "Kreon", Georgia, serif; font-weight: 400; }
  .brand-dot { width: 40px; height: 40px; border-radius: 50%; background: var(--cyan); margin: 0 auto 38px; }
  .brand-name { font-size: 32px; letter-spacing: 4px; line-height: 1; }
  .brand-sub { font-size: 21px; letter-spacing: 3px; margin-top: 10px; line-height: 1; color: var(--cyan); }

  .bubbles { position: absolute; left: 0; top: 0; }
  .bubble-text {
    position: absolute; display: flex; align-items: center; justify-content: center;
    text-align: center; color: #fff; font-family: "Kreon", Georgia, serif; font-weight: 300;
    font-size: 26px; line-height: 1.0; white-space: nowrap;
  }
  .bubble-identity { left: 324px; top: 308px; width: 180px; height: 172px; color: #e6f2fb; }
  .bubble-intimacy { left: 531px; top: 240px; width: 200px; height: 140px; }
  .bubble-career { left: 546px; top: 448px; width: 170px; height: 184px; color: var(--navy); }

  .headline {
    position: absolute; left: 42px; top: 550px; white-space: nowrap;
    font-family: "Kreon", Georgia, serif; font-weight: 400;
    font-size: 45px; line-height: 56px; color: var(--cyan);
  }
  .subline {
    position: absolute; left: 440px; top: 640px; white-space: nowrap;
    font-family: "Kreon", Georgia, serif; font-weight: 300; font-size: 33px; line-height: 38px; color: var(--navy);
  }
  .section-title {
    position: absolute; left: 48px; top: 770px; white-space: nowrap;
    font-family: "Kreon", Georgia, serif; font-weight: 300; font-size: 32px; color: var(--navy);
  }
  .section-rule { position: absolute; left: 48px; top: 813px; }

  .testimonials-label {
    position: absolute; left: 51px; top: 866px;
    font-family: "Kreon", Georgia, serif; font-weight: 300;
    font-size: 16px; letter-spacing: 0.5px; color: var(--cyan); text-transform: uppercase;
  }
  .quote {
    position: absolute; white-space: nowrap; font-style: italic;
    font-size: 17px; line-height: 22px; color: var(--quote);
  }
  .quote-1 { left: 51px; top: 893px; }
  .quote-2 { left: 51px; top: 990px; }
  .quote-3 { left: 448px; top: 854px; }
  .quote-4 { left: 448px; top: 943px; }
  .quote-5 { left: 448px; top: 1032px; }
</style>
</head>
<body>
  <main class="flyer">
    <div class="hero-photo" role="img" aria-label="Photograph of a woman in quiet contemplation, hand resting on her head, in a soft bright room"></div>
    <div class="hero-band"></div>

    <div class="brand">
      <div class="brand-dot"></div>
      <div class="brand-name">MERLOW</div>
      <div class="brand-sub">COACHING</div>
    </div>

    <svg class="bubbles" width="780" height="700" viewBox="0 0 780 700" aria-hidden="true">
      <path d="M414 286 a110 104 0 1 1 55 195 L490 508 L440 496 a110 104 0 0 1 -26 -210z" fill="var(--navy)"/>
      <ellipse cx="631" cy="317" rx="111" ry="104" fill="var(--purple)"/>
      <path d="M560 395 L556 438 L600 414 z" fill="var(--purple)"/>
      <circle cx="636" cy="535" r="110" fill="var(--cyan)"/>
      <path d="M680 440 L713 415 L716 480 z" fill="var(--cyan)"/>
    </svg>

    <div class="bubble-text bubble-identity">I’ve lost my<br>identity and<br>wondering<br>what life is<br>about.</div>
    <div class="bubble-text bubble-intimacy">I want more<br>intimacy in<br>my relationship.</div>
    <div class="bubble-text bubble-career">I hate my<br>career and<br>don’t know<br>what’s right<br>for me.</div>

    <h1 class="headline">Do you want a more<br>fulfilling and<br>meaningful life?</h1>
    <p class="subline">Make 2015 a year<br>for positive change</p>

    <h2 class="section-title">Personal Development Coaching can help you:</h2>
    <svg class="section-rule" width="672" height="20" viewBox="0 0 672 20" aria-hidden="true">
      <rect x="0" y="0" width="672" height="2" fill="var(--cyan)"/>
      <path d="M10 2 L34 2 L22 18 z" fill="var(--cyan)"/>
    </svg>

    <p class="testimonials-label">Testimonials from our clients:</p>
    <p class="quote quote-1">‘I have changed the way I approach<br>my daily life in order to achieve<br>more for myself’.</p>
    <p class="quote quote-2">‘Coaching has helped me change<br>the way I think, focusing more<br>on positive rather than negative<br>thoughts’.</p>
    <p class="quote quote-3">‘Without coaching, I believe that<br>my life would have remained<br>stagnant’.</p>
    <p class="quote quote-4">‘ I have made the leap to set up<br>my own business and have<br>increased my income three fold’.</p>
    <p class="quote quote-5">‘Coaching has helped me to grow<br>closer than ever to my husband’.</p>
  </main>
</body>
</html>
```